Business Card Design for Property Development Company Director

I am looking for a professional and unforgettable business card design for our Director of our Property Development Company.
Please see attached .pptx file to find out what information to include. You don't have to follow the exact format shown in the file - I am interested to see your creative flair using the information provided.

```html
<!DOCTYPE html>
<html lang="en">
<head>
<meta charset="utf-8">
<title>Marlow Property Group – Business Card</title>
<link rel="stylesheet" href="https://fonts.googleapis.com/css2?family=Roboto:wght@400;500;700&display=swap">
<style>
  :root {
    --brand-blue: #13509a;
    --brand-grey: #5d5e60;
    --band-grey: #c9c9ca;
    --card-white: #f6f6f4;
    --text-dark: #3a3a3c;
    --backdrop: #e4e1dc;
  }
  * { box-sizing: border-box; margin: 0; padding: 0; }
  html, body { width: 900px; height: 1200px; overflow: hidden; }
  body {
    background: var(--backdrop);
    font-family: "Roboto", Arial, sans-serif;
    position: relative;
  }
  .card {
    position: absolute;
    border-radius: 18px;
    overflow: hidden;
    box-shadow: 0 4px 14px rgba(0,0,0,0.18);
  }
  /* Front */
  .card-front { left: 86px; top: 137px; width: 737px; height: 432px; background: var(--card-white); }
  .wordmark {
    position: absolute; left: 38px; top: 60px;
    display: flex; align-items: center; gap: 16px;
    color: var(--brand-blue); font-weight: 700;
  }
  .wordmark-square { width: 80px; height: 98px; background: var(--brand-grey); }
  .wordmark-text { line-height: 1; }
  .wordmark-name { display: block; font-size: 66px; letter-spacing: 1px; }
  .wordmark-sub { display: block; font-size: 24px; letter-spacing: 3.4px; margin-top: 6px; }
  .name-band {
    position: absolute; left: 0; right: 0; top: 215px; height: 33px;
    background: var(--brand-blue); color: #fff;
    text-align: right; padding-right: 30px;
    font-size: 25px; line-height: 33px; font-weight: 400;
  }
  .name-band strong { font-weight: 700; }
  .title-band {
    position: absolute; left: 0; right: 0; top: 255px; height: 18px;
    background: var(--band-grey);
  }
  .title-label {
    position: absolute; right: 26px; top: -7px;
    background: var(--card-white); color: var(--text-dark);
    font-size: 21px; line-height: 30px; padding: 0 4px 0 10px;
  }
  .contact-list {
    position: absolute; right: 28px; top: 306px;
    list-style: none; text-align: right; color: var(--text-dark);
    font-size: 18px; letter-spacing: 0.4px;
  }
  .contact-list li { display: flex; justify-content: flex-end; align-items: center; gap: 12px; height: 34px; }
  .contact-icon { width: 22px; height: 18px; fill: var(--brand-blue); }
  .licence { position: absolute; left: 35px; top: 358px; font-size: 16px; line-height: 22px; }
  .licence-label { color: var(--brand-blue); }
  .licence-label strong { font-weight: 700; }
  .licence-number { color: var(--brand-grey); }
  /* Back */
  .card-back { left: 82px; top: 631px; width: 741px; height: 432px; background: var(--brand-grey); }
  .back-top { position: absolute; left: 0; right: 0; top: 0; height: 217px; background: var(--brand-blue); }
  .back-heading, .back-cta {
    position: absolute; left: 0; right: 0; text-align: center;
    color: #fff; font-weight: 700; font-size: 28px; line-height: 34px;
  }
  .back-heading { top: 55px; }
  .back-cta { top: 306px; line-height: 33.5px; }
  .back-wordmark {
    position: absolute; left: 167px; top: 164px; width: 405px; height: 105px;
    background: var(--card-white); border-radius: 10px;
    display: flex; align-items: center; justify-content: center; gap: 14px;
    color: var(--brand-blue); font-weight: 700;
  }
  .back-wordmark .wordmark-square { width: 60px; height: 76px; }
  .back-wordmark .wordmark-name { font-size: 50px; }
  .back-wordmark .wordmark-sub { font-size: 18px; letter-spacing: 2.6px; margin-top: 4px; }
</style>
</head>
<body>
  <section class="card card-front" aria-label="Business card front">
    <div class="wordmark">
      <span class="wordmark-square"></span>
      <span class="wordmark-text">
        <span class="wordmark-name">MARLOW</span>
        <span class="wordmark-sub">PROPERTY GROUP</span>
      </span>
    </div>
    <div class="name-band">DANIEL <strong>PRESCOTT</strong></div>
    <div class="title-band"><span class="title-label">Director</span></div>
    <ul class="contact-list">
      <li>0400 123 456
        <svg class="contact-icon" viewBox="0 0 24 20" aria-hidden="true"><path d="M2 7c0-3 4-5 10-5s10 2 10 5v2h-5V7c-1-1-3-1.5-5-1.5S8 6 7 7v2H2z"/><path d="M6 10l3-3h6l3 3v7H6z M12 11a2.2 2.2 0 1 0 0 4.4 2.2 2.2 0 0 0 0-4.4z"/></svg>
      </li>
      <li>daniel@marlow.com.au
        <svg class="contact-icon" viewBox="0 0 24 18" aria-hidden="true"><path d="M1 2h22v14H1z M3 4v1l9 6 9-6V4l-9 6z" fill-rule="evenodd"/></svg>
      </li>
      <li>www.marlow.com.au
        <svg class="contact-icon" viewBox="0 0 20 20" aria-hidden="true"><circle cx="10" cy="10" r="8.5" fill="none" stroke="#13509a" stroke-width="1.6"/><ellipse cx="10" cy="10" rx="3.6" ry="8.5" fill="none" stroke="#13509a" stroke-width="1.4"/><path d="M1.5 10h17M3 5.5h14M3 14.5h14" stroke="#13509a" stroke-width="1.3"/></svg>
      </li>
    </ul>
    <div class="licence">
      <div class="licence-label">Real Estate <strong>LIC</strong></div>
      <div class="licence-number">1234567 &amp; 1234568</div>
    </div>
  </section>

  <section class="card card-back" aria-label="Business card back">
    <div class="back-top"></div>
    <h2 class="back-heading">PROPERTY DEVELOPMENT<br>&amp; SITE ACQUISITION SPECIALISTS</h2>
    <div class="back-wordmark">
      <span class="wordmark-square"></span>
      <span class="wordmark-text">
        <span class="wordmark-name">MARLOW</span>
        <span class="wordmark-sub">PROPERTY GROUP</span>
      </span>
    </div>
    <p class="back-cta">ASK ME ABOUT<br>OUR INVESTMENT &amp; PARTNERSHIP<br>OPPORTUNITIES</p>
  </section>
</body>
</html>
```